Stationary for Financial Service Company
Business Card and Letterhead + Kit Folder
Stationary for Financial Service Company - Financial Services
Creative Brief
Simple
Brent Halvorsen
President
415 Kestrel Lane, Suite 308 Ottawa, ON
b.halvorsen@halvorseninc.example
www.capitalpathways.example
Steady Growth, Clear Choices
halvorsencapital halvorsencapital
In regards to the letterhead, please leave the background blank. Imaging behind the text is distracting. The contact information as the footer, with the logo centered as the header. Of the designs currently submitted, #153 is preferred, offering a simple, clean design. For the business cards, so far #50 (without the extra logo in the bottom right of the card) and #51 are the design concepts of interest.

```html
<!DOCTYPE html>
<html lang="en">
<head>
<meta charset="utf-8">
<title>Capital Pathways – Stationery Concepts</title>
<link href="https://fonts.googleapis.com/css2?family=Tinos:ital,wght@0,400;0,700;1,700&family=Arimo:wght@400&display=swap" rel="stylesheet">
<style>
  :root{
    --bg:#ebe5dc;
    --blue:#24459a;
    --blue-deep:#1c3580;
    --blue-light:#3464bd;
    --grey:#7d7d7d;
    --ink:#333;
    --white:#fff;
  }
  *{box-sizing:border-box;margin:0;padding:0}
  html,body{width:1200px;height:344px;overflow:hidden;background:var(--bg)}
  body{position:relative;font-family:"Arimo",Arial,sans-serif;color:var(--ink)}
  .item{position:absolute}
  .label{position:absolute;font-family:"Tinos","Times New Roman",serif;font-size:5.6px;color:#222;text-align:center;width:160px;margin-left:-80px;white-space:nowrap}

  /* brand lockup: plain name with one circle */
  .brand{display:flex;align-items:center;gap:.4em;font-family:"Tinos","Times New Roman",serif}
  .brand-mark{width:1.7em;height:1.7em;border-radius:50%;background:var(--blue);flex:none}
  .brand-name{display:block;font-size:1em;color:var(--blue);letter-spacing:.04em;text-transform:uppercase;line-height:1;white-space:nowrap}

  /* contact block */
  .contact{display:flex;justify-content:center;gap:.8em;font-size:3.3px;line-height:1.45;white-space:nowrap}
  .contact .who{text-align:right;padding-right:.8em;border-right:.25px solid var(--ink)}
  .contact .who b{display:block;font-family:"Tinos",serif;font-size:1.35em;color:var(--blue-deep);line-height:1.2}
  .contact .who i{display:block;font-family:"Tinos",serif;font-style:normal;color:#999;margin-bottom:.4em}
  .contact .lines span{display:flex;align-items:center;gap:.4em}
  .ico{width:1em;height:1em;fill:var(--blue-deep);flex:none}

  /* business cards */
  .card{width:131px;height:74px;background:var(--white);border-radius:3px;overflow:hidden;box-shadow:0 1px 2px rgba(0,0,0,.2)}
  .card .brand{font-size:6px;justify-content:center;margin-top:10px}
  .card .contact{margin-top:10px}
  .card-band{position:absolute;left:0;right:0;bottom:0;height:7px;background:var(--blue-deep);color:var(--white);font-size:2.8px;letter-spacing:.15em;text-align:center;line-height:7px}
  .card-band.thin{height:4px}
  .back{display:flex;flex-direction:column;align-items:center;justify-content:center;gap:9px}
  .back .brand{font-size:7px;margin:0}
  .back-blue{background:linear-gradient(135deg,var(--blue-light),var(--blue-deep))}
  .back-grey{background:var(--grey)}
  .back-blue .brand-name,.back-grey .brand-name{color:var(--white)}
  .back-blue .brand-mark,.back-grey .brand-mark{background:var(--white)}
  .back-slogan{font-family:"Tinos",serif;font-weight:700;font-style:italic;font-size:3.8px;color:var(--white)}
  .back-white .back-slogan{color:var(--blue)}

  /* title */
  .concepts{left:30px;top:80px;text-align:center}
  .concepts .brand{font-size:7.5px}
  .concepts h1{font-family:"Tinos",serif;font-weight:400;font-size:6.8px;color:#222;margin-top:9px}

  /* letterhead */
  .letterhead{left:310px;top:43px;width:220px;height:283px;background:var(--white);box-shadow:0 1px 2px rgba(0,0,0,.2)}
  .letterhead .brand{font-size:6px;justify-content:center;margin-top:10px}
  .letter-foot{position:absolute;left:0;right:0;bottom:6px;text-align:center;font-size:2.8px;line-height:1.8;white-space:nowrap}

  /* email signature */
  .signature{left:575px;top:16px;width:146px;height:69px;background:var(--white);box-shadow:0 1px 2px rgba(0,0,0,.2)}
  .signature .brand{font-size:6.5px;justify-content:center;margin-top:11px}
  .signature .contact{margin-top:10px}

  /* envelopes */
  .envelope{width:237px;background:var(--white);box-shadow:0 1px 2px rgba(0,0,0,.2)}
  .env-flap{height:34px;border-radius:0 0 6px 6px;display:flex;align-items:center;justify-content:center}
  .env-flap .brand-name{font-size:6px;color:var(--white);font-family:"Tinos",serif}
  .flap-blue{background:linear-gradient(90deg,var(--blue-deep),var(--blue-light),var(--blue-deep))}
  .flap-grey{background:var(--grey)}
  .flap-white{background:linear-gradient(#fff,#eee);border-bottom:.5px solid #ccc}
  .flap-white .brand-name{color:var(--blue)}
  .env-front .brand{font-size:6px;margin:12px 0 0 9px}
  .env-front .env-address{font-size:2.9px;margin:4px 0 0 30px}

  /* folder */
  .folder-tab{background:var(--grey);width:12px;height:202px;top:50px}
  .folder-tab span{position:absolute;left:50%;top:50px;transform:translate(-50%,-50%) rotate(-90deg);font-size:2.6px;letter-spacing:.12em;color:var(--white);white-space:nowrap}
  .folder-cover{top:50px;width:162px;height:202px}
  .cover-blue{left:834px;background:linear-gradient(160deg,var(--blue-light),var(--blue-deep))}
  .cover-white{left:996px;background:var(--white);display:flex;align-items:center;justify-content:center;padding-bottom:50px}
  .cover-white .brand{font-size:7.5px}
  .cover-contact{position:absolute;left:14px;top:162px;font-size:3px;color:var(--white);line-height:1.55;white-space:nowrap}
  .cover-contact .ico{fill:var(--white)}
  .cover-contact span{display:flex;align-items:center;gap:2px}
  .pocket{top:252px;height:76px;width:139px;background:linear-gradient(160deg,var(--blue-light),var(--blue-deep))}
  .pocket-left{left:846px;border-bottom-right-radius:10px}
  .pocket-right{left:1007px;border-bottom-left-radius:10px}
  .mini-card{left:1048px;top:272px;width:66px;height:37px;transform:rotate(-9deg);background:var(--white);border-radius:2px;box-shadow:0 1px 2px rgba(0,0,0,.3)}
  .mini-card .brand{font-size:3px;justify-content:center;margin-top:5px}
  .mini-card .contact{font-size:1.7px;margin-top:5px}
</style>
</head>
<body>
<svg width="0" height="0" style="position:absolute" aria-hidden="true">
  <symbol id="i-phone" viewBox="0 0 10 10"><path d="M2 1h2l1 2.5-1.3 1a6 6 0 0 0 2.8 2.8l1-1.3L10 7v2c0 .6-.4 1-1 1A9 9 0 0 1 0 1c0-.6.4-1 1-1z"/></symbol>
  <symbol id="i-fax" viewBox="0 0 10 10"><path d="M2 0h5l1 1v3h1.5v6h-9V4H2zm1 1v3h4V1zM2 6v1h6V6z"/></symbol>
  <symbol id="i-mail" viewBox="0 0 10 10"><path d="M0 2h10v6H0zm1 .8L5 5.5l4-2.7V3L5 5.8 1 3z"/></symbol>
</svg>

<div class="item concepts">
  <div class="brand"><span class="brand-mark"></span><span class="brand-name">Capital Pathways</span></div>
  <h1>Stationary Concepts</h1>
</div>

<div class="item card" style="left:164px;top:59px">
  <div class="brand"><span class="brand-mark"></span><span class="brand-name">Capital Pathways</span></div>
  <div class="contact">
    <div class="who"><b>Brent Halvorsen</b><i>President</i>415 Kestrel Lane<br>Suite 308, Ottawa, ON</div>
    <div class="lines">
      <span><svg class="ico"><use href="#i-phone"/></svg>1-888-555-0142</span>
      <span><svg class="ico"><use href="#i-phone"/></svg>613-555-0188</span>
      <span><svg class="ico"><use href="#i-fax"/></svg>613-555-0187</span>
      <span><svg class="ico"><use href="#i-mail"/></svg>b.halvorsen@halvorseninc.example</span>
    </div>
  </div>
  <div class="card-band">www.capitalpathways.example</div>
</div>

<div class="item card back back-blue" style="left:19px;top:159px">
  <div class="brand"><span class="brand-mark"></span><span class="brand-name">Capital Pathways</span></div>
  <div class="back-slogan">Steady Growth, Clear Choices</div>
</div>
<div class="label" style="left:84px;top:238px">Back Card Option_01</div>

<div class="item card" style="left:165px;top:159px">
  <div class="brand"><span class="brand-mark"></span><span class="brand-name">Capital Pathways</span></div>
  <div class="contact">
    <div class="who"><b>Brent Halvorsen</b><i>President</i>415 Kestrel Lane<br>Suite 308, Ottawa, ON</div>
    <div class="lines">
      <span><svg class="ico"><use href="#i-phone"/></svg>1-888-555-0142</span>
      <span><svg class="ico"><use href="#i-phone"/></svg>613-555-0188</span>
      <span><svg class="ico"><use href="#i-fax"/></svg>613-555-0187</span>
      <span><svg class="ico"><use href="#i-mail"/></svg>b.halvorsen@halvorseninc.example</span>
    </div>
  </div>
  <div class="card-band thin"></div>
</div>
<div class="label" style="left:227px;top:238px">Front Card</div>

<div class="item card back back-white" style="left:19px;top:253px">
  <div class="brand"><span class="brand-mark"></span><span class="brand-name">Capital Pathways</span></div>
  <div class="back-slogan">Steady Growth, Clear Choices</div>
</div>
<div class="label" style="left:84px;top:331px">Back Card Option_02</div>

<div class="item card back back-grey" style="left:165px;top:253px">
  <div class="brand"><span class="brand-mark"></span><span class="brand-name">Capital Pathways</span></div>
  <div class="back-slogan">Steady Growth, Clear Choices</div>
</div>
<div class="label" style="left:230px;top:331px">Back Card Option_03</div>

<div class="item letterhead">
  <div class="brand"><span class="brand-mark"></span><span class="brand-name">Capital Pathways</span></div>
  <div class="letter-foot">415 Kestrel Lane, Suite 308, Ottawa, ON<br>P : 1-888-555-0142 &nbsp;P : 613-555-0188 &nbsp;F : 613-555-0187 &nbsp;E : b.halvorsen@halvorseninc.example &nbsp;W : www.capitalpathways.example</div>
</div>
<div class="label" style="left:416px;top:331px">Letterhead option_02</div>

<div class="item signature">
  <div class="brand"><span class="brand-mark"></span><span class="brand-name">Capital Pathways</span></div>
  <div class="contact">
    <div class="who"><b>Brent Halvorsen</b><i>President</i>415 Kestrel Lane<br>Suite 308, Ottawa, ON</div>
    <div class="lines">
      <span><svg class="ico"><use href="#i-phone"/></svg>1-888-555-0142</span>
      <span><svg class="ico"><use href="#i-phone"/></svg>613-555-0188</span>
      <span><svg class="ico"><use href="#i-fax"/></svg>613-555-0187</span>
      <span><svg class="ico"><use href="#i-mail"/></svg>b.halvorsen@halvorseninc.example</span>
    </div>
  </div>
</div>
<div class="label" style="left:643px;top:91px">Email Signature</div>

<div class="item envelope" style="left:544px;top:103px;height:141px"><div class="env-flap flap-blue"><span class="brand-name">Capital Pathways</span></div></div>
<div class="item envelope" style="left:566px;top:142px;height:146px"><div class="env-flap flap-grey"><span class="brand-name">Capital Pathways</span></div></div>
<div class="item envelope" style="left:550px;top:185px;height:112px"><div class="env-flap flap-white"><span class="brand-name">Capital Pathways</span></div></div>
<div class="item envelope env-front" style="left:538px;top:223px;height:103px">
  <div class="brand"><span class="brand-mark"></span><span class="brand-name">Capital Pathways</span></div>
  <div class="env-address">415 Kestrel Lane, Suite 308, Ottawa, ON</div>
</div>
<div class="label" style="left:650px;top:331px">Envelope &nbsp;Front</div>

<div class="item folder-tab" style="left:822px"><span>www.capitalpathways.example</span></div>
<div class="item folder-cover cover-blue">
  <div class="cover-contact">
    415 Kestrel Lane<br>Suite 308, Ottawa, ON
    <span style="margin-top:3px"><svg class="ico"><use href="#i-phone"/></svg>1-888-555-0142</span>
    <span><svg class="ico"><use href="#i-phone"/></svg>613-555-0188</span>
    <span><svg class="ico"><use href="#i-fax"/></svg>613-555-0187</span>
    <span><svg class="ico"><use href="#i-mail"/></svg>b.halvorsen@halvorseninc.example</span>
  </div>
</div>
<div class="item folder-cover cover-white">
  <div class="brand"><span class="brand-mark"></span><span class="brand-name">Capital Pathways</span></div>
</div>
<div class="item folder-tab" style="left:1158px"><span>www.capitalpathways.example</span></div>
<div class="item pocket pocket-left"></div>
<div class="item pocket pocket-right"></div>
<div class="item mini-card">
  <div class="brand"><span class="brand-mark"></span><span class="brand-name">Capital Pathways</span></div>
  <div class="contact">
    <div class="who"><b>Brent Halvorsen</b><i>President</i>415 Kestrel Lane<br>Suite 308, Ottawa, ON</div>
    <div class="lines">
      <span>1-888-555-0142</span><span>613-555-0188</span><span>613-555-0187</span><span>b.halvorsen@halvorseninc.example</span>
    </div>
  </div>
</div>
<div class="label" style="left:996px;top:331px">Folder</div>
</body>
</html>
```